Modern home page design for a Dental Surgery

- This design will have a 5 day deadline only.

- The design must be based around the attached HPID (home page information design) called LUMA HPID. I've attached Word and PDF versions - these are the same. The table boxes are just for approximate placement of information – you DON'T have to make it look exactly like this. All fonts used in the HPID are only examples - you can use any Google font you wish.

- Information only is in orange text. Copy to go on the design in black text. Some instructions are in the HPID. Please be creative!

- The design needs to be modern. Colours are to be black and white with grey and blue like the logo colours. Background white please.

- I've provided the images for the galleries - they are labelled and will match the name in the HPID.

- I've provided icons for the items below the gallery - the name of the image will match the subheading for each section. You can use other icons if you want to.

- This is a website that is an example of what we like. Please DON'T copy this exactly though!
http://brightmolarclinic.example.co.nz/

Width of content will be 1100 pixels when implemented as a web page. Header height (without nav bar) 150-160 pixels.

If your design is chosen the winning PSD file will have to be provided as follows…
1. Canvas size of 2000px x 2000px - 72ppi in Adobe Photoshop (CS5 compatible)
2. Width of content section is 1100px wide - centered in the canvas
3. Any button rollovers/hovers in the PSD as hidden layers.
4. All fonts used must be Google fonts (except for the fonts in the header at the top of the page).
5. You will need to supply the chosen home page plus one example page (example page as a style guide for how all other pages will look). Example page is only the header and navigational bar at the top, an empty sector in the middle with a column (180 px wide) which can be left or right aligned which means the main sector is 920 pixels wide, and then the footer at the bottom of the page
Updates

Hi Designers, The 1st posted deadline for this project was incorrect; please note new deadline for November 22.

Target Market(s)

all ages that need dental care

Industry/Entity Type

Dental

Number of Pages Required

1 page

Font styles to use
Sans Serif

Requirements
Must have
• modern clean design - as per the Project Description
Should not have
• should not be cluttered. Just because I use tables to show information placement on the HPID - you do NOT have to use boxes around information in the design.

```html
<!DOCTYPE html>
<html lang="en">
<head>
<meta charset="utf-8">
<title>Bright Molar Clinic – Home</title>
<link href="https://fonts.googleapis.com/css2?family=Lato:wght@400;700&display=swap" rel="stylesheet">
<style>
:root{
  --ink:#111;
  --text:#333;
  --muted:#777;
  --grey:#a7a7a9;
  --rule:#e2e2e2;
  --red:#f05252;
  --alert:#e8141b;
  --teal:#0f6d77;
  --teal-dark:#0b4f58;
  --white:#fff;
}
*{margin:0;padding:0;box-sizing:border-box}
html,body{width:1200px;height:900px;overflow:hidden;background:var(--white)}
body{position:relative;font-family:'Lato',sans-serif;color:var(--text)}
.abs{position:absolute}
.brand{left:374px;top:3px;color:var(--muted);line-height:1}
.brand-name{font-size:13px;display:block;line-height:13px;white-space:nowrap}
.brand-sub{font-size:5px;display:block;margin-top:2px;padding-left:24px}
.location{left:577px;top:4px;font-size:6.5px;line-height:10.5px;color:var(--ink)}
.phone-top{left:764px;top:4px;text-align:center;width:74px}
.phone-top span{display:block;font-size:10px;color:var(--ink);margin-top:2px;white-space:nowrap}
.nav{left:336px;top:40px;width:529px;height:25px;background:var(--grey);display:flex;justify-content:space-around;align-items:center;padding:0 20px}
.nav a{font-size:6.5px;color:var(--ink);text-decoration:none;position:relative;height:25px;line-height:25px;white-space:nowrap}
.nav a.current::after{content:"";position:absolute;left:-4px;right:-4px;bottom:0;height:2px;background:var(--red)}
.hero{left:336px;top:65px;width:529px;height:193px;background:radial-gradient(ellipse at 55% 60%,#4a4f55 0%,#2b2e32 50%,#1a1b1d 100%);text-align:center;color:var(--white)}
.hero h1{font-size:12.5px;font-weight:700;margin-top:45px}
.hero h1 em{font-style:normal;color:var(--red);font-weight:400}
.hero p{font-size:5.3px;line-height:9px;width:300px;margin:10px auto 0}
.btn{display:inline-block;background:var(--red);color:var(--white);font-size:6.5px;text-transform:uppercase;text-align:center;text-decoration:none;white-space:nowrap}
.hero .btn{width:68px;height:18px;line-height:18px;margin-top:14px;font-size:8px}
.icon{width:14px;height:16px}
.title{font-weight:700;color:var(--ink);white-space:nowrap}
.copy{font-size:6.4px;line-height:10.5px;color:var(--ink)}
.vline{width:1px;background:var(--rule)}
.hline{left:336px;width:529px;height:1px;background:var(--rule)}
.big-title{font-size:10px}
.mid-title{font-size:8px}
.assoc{left:336px;top:620px;width:529px;height:60px}
.footer-col{top:712px;color:var(--ink);white-space:nowrap}
.footer-col ul{list-style:none}
.footer-col li{font-size:8px;line-height:12px}
.footer-col .head{font-weight:700;font-size:7px}
.col-nav li{line-height:13px}
.col-nav .gap{margin-top:3.5px}
.col-svc .gap{margin-top:2px}
.col-more .gap{margin-top:5px}
.dot::before{content:"•  ";color:var(--red)}
.ddot::before{content:"••  ";color:var(--red);font-size:7px}
.footer-col .sub{font-size:7px;line-height:11.2px;color:var(--text)}
.footer-col .tiny{font-size:5.3px;line-height:9px;color:var(--text);padding-left:3px}
.tiny::before{content:"->  "}
.bottom{left:336px;top:875px;width:529px;height:25px;background:var(--grey)}
.legal{left:376px;top:883px;font-size:5.5px;color:var(--ink);white-space:nowrap}
</style>
</head>
<body>

<header>
  <div class="abs brand">
    <span class="brand-name">Bright Molar</span>
    <span class="brand-name">Clinic</span>
    <span class="brand-sub">Dr Ana Morel</span>
  </div>
  <div class="abs location">Northvale<br>Family Dental<br>NORTHVALE</div>
  <div class="abs phone-top">
    <svg width="16" height="14" viewBox="0 0 16 14" aria-hidden="true"><path d="M1 5 Q8 -1 15 5 L13 7 L11 5 L5 5 L3 7Z M4 6 L12 6 L14 13 L2 13Z" fill="#111"/><circle cx="8" cy="9.5" r="2" fill="#fff"/></svg>
    <span>04 555 0192</span>
  </div>
</header>

<nav class="abs nav">
  <a class="current">Home</a><a>About</a><a>What We Do</a><a>Why Choose Us</a><a>Services</a><a>Costs</a><a>Appointment</a><a>Contact/Map</a>
</nav>

<section class="abs hero" role="img" aria-label="Darkened photo of a modern dental surgery room">
  <h1>Need An Expert Caring <em>Dentist?</em></h1>
  <p>Lorem ipsum dolor sit amet, consectetur adipiscing elit. Phasellus congue quis magna at convallis. Donec hendrerit fringilla urna, in placerat lacus blandit a. Suspendisse sapien justo, scelerisque id egestas vehicula, egestas sed dolor. Maecenas arcu augue, consequat non facilisis a, maximus vel diam trices.</p>
  <a class="btn">Call Us</a>
</section>

<svg class="abs icon" style="left:375px;top:266px" viewBox="0 0 14 16" aria-hidden="true"><circle cx="7" cy="4" r="3" fill="none" stroke="#1b6fb5" stroke-width="1.4"/><path d="M7 7 V11 Q7 14 10 14" fill="none" stroke="#111" stroke-width="1.2"/><circle cx="11" cy="14" r="1.3" fill="#111"/></svg>
<h2 class="abs title big-title" style="left:403px;top:270px">What We Do ?</h2>
<p class="abs copy" style="left:403px;top:288px;width:180px">The Bright Molar Dental Team offer a wide range of dental services including diagnostics, orthodontics, dentures, oral surgery, and periodontal, root canal and cosmetic dentistry.</p>
<a class="abs btn" style="left:524px;top:329px;width:54px;height:17px;line-height:17px">More</a>

<div class="abs vline" style="left:600px;top:265px;height:90px"></div>

<svg class="abs icon" style="left:605px;top:266px" viewBox="0 0 14 16" aria-hidden="true"><path d="M2 3 Q3 0 7 2 Q11 0 12 3 Q13 7 10 15 L8.5 9 L5.5 9 L4 15 Q1 7 2 3Z" fill="none" stroke="#1b6fb5" stroke-width="1.2"/></svg>
<h2 class="abs title big-title" style="left:630px;top:270px">How much does it Cost?</h2>
<p class="abs copy" style="left:630px;top:288px;width:185px">Find out estimates of how much each dental procedure costs. (Exact prices will be discussed with you after consultation depending on your specific dental requirements.)</p>
<a class="abs btn" style="left:756px;top:329px;width:54px;height:17px;line-height:17px">Costs</a>

<div class="abs hline" style="top:367px"></div>

<svg class="abs icon" style="left:373px;top:389px;width:18px" viewBox="0 0 18 16" aria-hidden="true"><rect x="2" y="6" width="14" height="8" rx="2" fill="#dde7f0" stroke="#1b6fb5"/><path d="M4 6 L9 2 L14 6" fill="none" stroke="#111"/></svg>
<h3 class="abs title mid-title" style="left:400px;top:391px">Make an Appointment</h3>
<p class="abs copy" style="left:400px;top:405px;width:122px">Two convenient locations in Eastbrook and Northvale dental services for all ages. Take moment to book your appointment.</p>
<a class="abs btn" style="left:461px;top:443px;width:53px;height:17px;line-height:17px;font-size:5.5px">Appointment</a>

<div class="abs vline" style="left:523px;top:376px;height:94px"></div>

<svg class="abs icon" style="left:527px;top:389px" viewBox="0 0 14 16" aria-hidden="true"><path d="M2 3 Q3 0 7 2 Q11 0 12 3 Q13 7 10 15 L8.5 9 L5.5 9 L4 15 Q1 7 2 3Z" fill="none" stroke="#1b6fb5" stroke-width="1.2"/></svg>
<h3 class="abs title mid-title" style="left:548px;top:391px">Your First Consultation</h3>
<p class="abs copy" style="left:548px;top:405px;width:120px">Want to know what will happen in your first consultation? Check out our first dental consultation process.</p>
<a class="abs btn" style="left:611px;top:443px;width:54px;height:17px;line-height:17px;font-size:5.5px">Consultation</a>

<div class="abs vline" style="left:673px;top:376px;height:94px"></div>

<svg class="abs icon" style="left:678px;top:389px" viewBox="0 0 14 16" aria-hidden="true"><rect x="2" y="1" width="10" height="13" fill="#dde7f0" stroke="#1b6fb5"/><path d="M4 5 H10 M4 8 H10 M4 11 H8" stroke="#111" stroke-width=".8"/></svg>
<h3 class="abs title mid-title" style="left:698px;top:391px">Application Form</h3>
<p class="abs copy" style="left:698px;top:405px;width:122px">Save time and fill in an online application form (or download, print out and complete) before your first visit.</p>
<a class="abs btn" style="left:765px;top:443px;width:53px;height:17px;line-height:17px;font-size:5.5px">Application</a>

<div class="abs hline" style="top:482px"></div>

<svg class="abs icon" style="left:378px;top:494px" viewBox="0 0 14 16" aria-hidden="true"><path d="M2 3 Q3 0 7 2 Q11 0 12 3 Q13 7 10 15 L8.5 9 L5.5 9 L4 15 Q1 7 2 3Z" fill="none" stroke="#111" stroke-width="1.2"/></svg>
<h3 class="abs title mid-title" style="left:400px;top:499px">Is This An Emergency?</h3>
<p class="abs copy" style="left:400px;top:517px;width:420px">Lorem ipsum dolor sit amet, consectetur adipiscing elit. Phasellus congue quis magna at convallis. Donec hendrerit fringilla urna, in placerat lacus blandit a. Suspendisse sapien justo, scelerisque id egestas vehicula, egestas sed dolor. Maecenas arcu augue, consequat non facilisis a, maximus vel diam. Sed a dapibus sapien, ut vestibulum mi. Duis ut metus lacinia neque aliquet pellentesque sed eget neque.</p>
<span class="abs" style="left:738px;top:558px;font-size:9.5px;color:var(--ink);white-space:nowrap">04 555 0192</span>
<svg class="abs" style="left:795px;top:542px" width="28" height="22" viewBox="0 0 28 22" aria-hidden="true"><ellipse cx="14" cy="10" rx="13" ry="9" fill="var(--alert)"/><path d="M6 16 L3 22 L11 18Z" fill="var(--alert)"/></svg>
<span class="abs" style="left:799px;top:548px;font-size:6px;color:var(--white);white-space:nowrap">Call us</span>

<div class="abs hline" style="top:586px"></div>

<h3 class="abs title" style="left:379px;top:597px;font-size:7.5px">Associations</h3>
<svg class="abs assoc" viewBox="0 0 529 60" aria-label="Association badges">
  <g fill="var(--teal)" stroke="var(--teal-dark)" stroke-width="1">
    <ellipse cx="62" cy="28" rx="24" ry="16"/>
    <ellipse cx="124" cy="28" rx="24" ry="16"/>
    <ellipse cx="186" cy="28" rx="24" ry="16"/>
    <ellipse cx="264" cy="28" rx="38" ry="24"/>
    <ellipse cx="341" cy="28" rx="24" ry="16"/>
    <ellipse cx="403" cy="28" rx="24" ry="16"/>
    <ellipse cx="465" cy="28" rx="24" ry="16"/>
  </g>
</svg>

<div class="abs hline" style="top:693px"></div>

<div class="abs footer-col col-nav" style="left:377px">
  <ul>
    <li class="head">Home</li>
    <li class="head gap">About</li>
    <li class="dot gap">Team</li>
    <li class="dot">Registration Form</li>
    <li class="head gap">What We Do</li>
    <li class="head gap">Why Choose Us</li>
    <li class="dot gap">Costs</li>
    <li class="dot">Appointment</li>
    <li class="dot">Contact / Map</li>
  </ul>
</div>
<div class="abs vline" style="left:486px;top:708px;height:152px"></div>
<div class="abs footer-col col-svc" style="left:490px">
  <ul>
    <li class="head">Services</li>
    <li class="ddot gap">Restorative Dentistry</li>
    <li class="ddot sub">Preventative</li>
    <li class="tiny">Fissure Sealants</li>
    <li class="tiny">Mouthguards</li>
    <li class="tiny">Bite Splints</li>
    <li class="ddot sub">Fillings</li>
    <li class="tiny">Amalgams, Composites (white fillings</li>
    <li class="tiny">Porcelain &amp; Gold</li>
    <li class="ddot sub">Crown &amp; Bridge Treatment</li>
    <li class="ddot sub">Implants</li>
    <li class="ddot gap">Dentures</li>
  </ul>
</div>
<div class="abs vline" style="left:600px;top:708px;height:152px"></div>
<div class="abs footer-col col-more" style="left:603px">
  <ul>
    <li class="dot">Oral Surgery</li>
    <li class="ddot sub">Extractions</li>
    <li class="ddot sub">Minor Impacted Wisdom</li>
    <li class="dot gap">Periodontal (gum) Care</li>
    <li class="ddot sub">Hygiene Services</li>
    <li class="ddot sub">Minor Periodontal Surgery</li>
    <li class="ddot sub">Preventative Services</li>
    <li class="dot gap">Root Canal Therapy</li>
    <li class="dot gap">Cosmetic</li>
    <li class="ddot sub">Porcelain Veneers</li>
    <li class="ddot sub">Light Whitening</li>
  </ul>
</div>
<div class="abs vline" style="left:713px;top:708px;height:152px"></div>
<div class="abs footer-col col-more" style="left:718px">
  <ul>
    <li class="dot">Orthodontics</li>
    <li class="dot">Children &amp; pre schoolers</li>
    <li class="sub">Secondary School Dentistry</li>
    <li class="sub">Free Dental Care Under 18</li>
    <li class="sub">Pre-school Dentistry</li>
    <li class="dot gap">Oral Care Products</li>
    <li class="dot gap">Diagnostic Dentistry</li>
    <li class="sub">Digital X rays</li>
    <li class="sub">Panoramic X-rays</li>
    <li class="sub">Intra-oral photography</li>
    <li class="sub">Laser Cavity Detection</li>
  </ul>
</div>

<footer>
  <div class="abs bottom"></div>
  <p class="abs legal">© &nbsp;All Right Reserved 2014 - Dental Surgery - Privacy Policy &nbsp;| &nbsp;Terms &amp; Conditions</p>
  <svg class="abs" style="left:776px;top:879px" width="52" height="16" viewBox="0 0 52 16" aria-label="Social links">
    <circle cx="8" cy="8" r="7.5" fill="#1a1a1a"/>
    <circle cx="26" cy="8" r="7.5" fill="#1a1a1a"/>
    <circle cx="44" cy="8" r="7.5" fill="#1a1a1a"/>
  </svg>
</footer>

</body>
</html>
```